Delvane Pitching Mechanics

Private pitching sessions with a Division 1 WJAL baseball pitcher. Would also like a page setup where clients can request sesseions and pay for sessions.

```html
<!DOCTYPE html>
<html lang="en">
<head>
<meta charset="utf-8">
<title>Delvane Pitching Mechanics</title>
<link href="https://fonts.googleapis.com/css2?family=Michroma&family=Manrope:wght@400;500;600;700;800&display=swap" rel="stylesheet">
<style>
:root{
  --red:#e41f26;
  --ink:#111111;
  --night:#03050a;
  --field:#141a0c;
  --blush:#fce8ea;
  --white:#ffffff;
  --text:#2a2a2a;
}
*{box-sizing:border-box;margin:0;padding:0}
html,body{width:1200px;height:4075px;overflow:hidden;background:var(--white)}
body{position:relative;font-family:"Manrope",sans-serif;color:var(--text)}
.abs{position:absolute}
.section-title{position:absolute;left:0;width:1200px;text-align:center;color:var(--red);font-size:27px;font-family:"Michroma",sans-serif;font-weight:400;letter-spacing:1px}

/* header */
.topbar{left:0;top:0;width:1200px;height:85px;background:var(--red)}
.brand{left:112px;top:20px;width:200px;color:var(--white);font-family:"Manrope",sans-serif;font-weight:800;font-size:19px;line-height:23px}
.contact-item{top:20px;color:var(--white);font-size:15px;font-weight:500}
.contact-item b{display:block;font-family:"Michroma",sans-serif;font-size:10px;font-weight:400;letter-spacing:1px;margin-bottom:6px}
.social{display:flex;gap:15px}
.social span{width:34px;height:34px;border-radius:50%;background:var(--white);border:3px solid var(--ink)}
.social.dark span{background:transparent;border:3px solid var(--white)}
.navbar{left:0;top:85px;width:1200px;height:54px}
.nav-links{left:0;top:103px;width:1200px;font-size:15px;font-weight:500;color:var(--ink)}
.nav-links span{position:absolute}
.nav-links .active{color:var(--red)}

/* hero */
.hero-photo{left:0;top:85px;width:1200px;height:576px}
.hero-copy{left:522px;top:352px;width:600px;color:var(--white)}
.hero-copy h1{font-family:"Michroma",sans-serif;font-weight:400;font-size:16.5px;letter-spacing:.8px;white-space:nowrap;margin-bottom:22px}
.hero-copy p{font-size:15px;line-height:32px}
.btn{position:absolute;height:54px;border-radius:27px;background:var(--red);border:3px solid var(--white);color:var(--white);font-family:"Michroma",sans-serif;font-size:12px;letter-spacing:.5px;white-space:nowrap;display:flex;align-items:center;padding-left:20px;box-shadow:0 0 0 2px var(--red)}
.btn svg{position:absolute;right:8px;top:4px}

/* about */
.about-text{left:112px;top:830px;width:437px;font-size:16px;line-height:32.6px;text-align:justify;color:var(--ink)}
.about-photo{left:601px;top:851px;width:487px;height:363px;border-radius:32px;background:linear-gradient(160deg,#8f9a6e,#6f7c4b 55%,#a4a686)}

/* stats */
.stats{left:0;top:1307px;width:1200px;height:443px;border-radius:40px;background:radial-gradient(ellipse at 55% 45%,#2c331f 0%,var(--field) 55%,#0c1007 100%)}
.stats h2{position:absolute;left:0;top:66px;width:1200px;text-align:center;color:var(--white);font-family:"Michroma",sans-serif;font-weight:400;font-size:24px;letter-spacing:1px}
.stat{position:absolute;top:141px;width:300px;color:var(--white)}
.stat-icon{width:77px;height:77px;border-radius:6px;background:var(--red);display:flex;align-items:center;justify-content:center}
.stat-num{position:absolute;left:112px;top:20px;font-family:"Michroma",sans-serif;font-size:26px}
.stat h3{margin-top:30px;font-family:"Michroma",sans-serif;font-weight:400;font-size:17px;letter-spacing:1px}
.stat p{margin-top:18px;font-size:16px;line-height:32px;text-align:justify}

/* team */
.team-player{left:134px;top:1847px;width:309px;height:469px;border-radius:150px 150px 20px 60px;background:linear-gradient(170deg,#d92e30 0%,#b8262a 45%,#d9d6d2 75%,#f1efec 100%)}
.team-intro{left:440px;top:1922px;width:564px;font-size:16px;line-height:33px;text-align:justify;color:var(--ink)}
.member{position:absolute;top:2019px;width:219px;height:297px;border-radius:8px}
.member.one{left:384px;background:linear-gradient(160deg,#e7ecef,#9aa7ae 60%,#3b4148)}
.member.two{left:612px;background:linear-gradient(170deg,#2a2421,#0e0c0b);color:var(--white);text-align:center}
.member.three{left:840px;background:linear-gradient(160deg,#5b3fa3,#3b3f8c 50%,#27306b)}
.member.two h4{margin-top:103px;font-family:"Michroma",sans-serif;font-weight:400;font-size:14px;letter-spacing:1px}
.member.two p{margin-top:14px;font-size:15px}
.member.two .social{justify-content:center;gap:12px;margin-top:18px}
.member.two .social span{width:28px;height:28px}
.dots{left:669px;top:2350px;display:flex;gap:8px}
.dots span{width:30px;height:4px;border-radius:2px;background:#f08e91}
.dots .on{background:var(--red)}

/* portfolio */
.tile{position:absolute;height:259px}
.t1{left:0;top:2522px;width:389px;background:linear-gradient(180deg,#b64a4b,#6f8f74 60%,#c7a57f)}
.t2{left:406px;top:2522px;width:389px;border-radius:6px;background:linear-gradient(180deg,#2b2d30,#1a1a1c);display:flex;align-items:center;justify-content:center}
.t3{left:809px;top:2522px;width:391px;background:linear-gradient(120deg,#e0d8c9,#8aa2c1 50%,#c4b28b)}
.t4{left:0;top:2798px;width:389px;height:258px;background:linear-gradient(160deg,#7c6f5c,#e8e3d9 55%,#8b7a62)}
.t5{left:406px;top:2798px;width:389px;height:258px;background:linear-gradient(160deg,#2a2f3a,#d7d7d7 50%,#4b5f3a)}
.t6{left:809px;top:2798px;width:391px;height:258px;background:linear-gradient(180deg,#5b7fa8,#2f4a3d 55%,#b07b5a)}

/* contact form */
.field{position:absolute;height:59px;background:var(--blush);border-radius:3px;font-size:15px;font-weight:500;color:#3a3a3a;padding:21px 0 0 25px}

/* footer */
.footer-bg{left:0;top:3620px;width:1200px;height:455px}
.footer-brand{left:0;top:3690px;width:1200px;text-align:center;color:var(--white);font-weight:800;font-size:26px;line-height:32px}
.f-item{position:absolute;top:3786px;color:var(--white);font-size:15px}
.f-item b{display:block;font-family:"Michroma",sans-serif;font-weight:400;font-size:11px;letter-spacing:1px;margin-bottom:10px}
.f-div{position:absolute;top:3786px;width:1px;height:52px;background:#555}
.f-nav{left:0;top:3884px;width:1200px;text-align:center;color:var(--white);font-size:15px;font-weight:500}
.f-nav i{font-style:normal;margin:0 18px}
.copy{left:0;top:4008px;width:1200px;text-align:center;color:var(--white);font-size:13px}
.copy i{font-style:normal;margin:0 12px}
</style>
</head>
<body>

<!-- hero background first so the nav sits above it -->
<svg class="abs hero-photo" width="1200" height="576" viewBox="0 0 1200 576" role="img" aria-label="Photo of a pitcher in a red jersey throwing under stadium lights">
  <defs>
    <radialGradient id="heroGlow" cx="0.35" cy="0.45" r="0.7">
      <stop offset="0" stop-color="#3f6a80"/>
      <stop offset="0.5" stop-color="#14303f"/>
      <stop offset="1" stop-color="#03070b"/>
    </radialGradient>
  </defs>
  <path d="M0 0H1200V484Q600 640 0 484z" fill="url(#heroGlow)"/>
</svg>

<!-- header -->
<div class="abs topbar"></div>
<div class="abs brand">Delvane Pitching Mechanics</div>
<svg class="abs" style="left:415px;top:32px" width="26" height="20" viewBox="0 0 26 20"><rect x="1" y="1" width="24" height="18" fill="none" stroke="#fff" stroke-width="2"/><path d="M1 1l12 10 12-10" fill="none" stroke="#fff" stroke-width="2"/></svg>
<div class="abs contact-item" style="left:465px"><b>EMAIL US</b>BOOK@DELVANEPM.COM</div>
<svg class="abs" style="left:670px;top:29px" width="24" height="24" viewBox="0 0 24 24"><path d="M5 2l4 5-2 3c1 3 4 6 7 7l3-2 5 4-3 4C10 22 2 14 1 5z" fill="none" stroke="#fff" stroke-width="2"/></svg>
<div class="abs contact-item" style="left:718px"><b>CALL US</b>+1 555 014 2200</div>
<div class="abs social" style="left:951px;top:26px"><span></span><span></span><span></span></div>

<svg class="abs navbar" viewBox="0 0 1200 54" width="1200" height="54"><rect width="1200" height="54" fill="#03070b"/><polygon points="119,0 1080,0 1048,54 151,54" fill="#fff"/></svg>
<div class="abs nav-links">
  <span class="active" style="left:305px">HOME</span>
  <span style="left:392px">ABOUT US</span>
  <span style="left:507px">TEAM</span>
  <span style="left:588px">PORTFOLIO</span>
  <span style="left:711px">CONTACT</span>
</div>
<svg class="abs" style="left:874px;top:102px" width="18" height="18" viewBox="0 0 18 18"><circle cx="7" cy="7" r="5.5" fill="none" stroke="#111" stroke-width="2.2"/><path d="M11 11l6 6" stroke="#111" stroke-width="2.4"/></svg>

<div class="abs hero-copy">
  <h1>DIVISION 1 WJAL BASEBALL PITCHER</h1>
  <p>Nemo enim ipsam voluptatem quia voluptas sit aspernatur aut odit<br>aut fugit, sed quia consequuntur magni dolores.</p>
</div>
<div class="btn" style="left:522px;top:492px;width:221px">GET STARTED
  <svg width="40" height="40" viewBox="0 0 40 40"><circle cx="22" cy="20" r="15" fill="#fff"/><path d="M16 9q8 11 2 22M25 6q7 12 1 27" fill="none" stroke="#e41f26" stroke-width="2"/></svg>
</div>

<!-- about -->
<h2 class="section-title" style="top:748px">ABOUT US</h2>
<p class="abs about-text">Neque porro quisquam est, qui dolorem ipsum quia dolor sit amet, consectetur, adipisci velit, sed quia non numquam eius modi tempora incidunt ut labore et dolore magnam aliquam quaerat voluptatem. Ut enim ad minima veniam, quis nostrum exercitationem ullam corporis suscipit laboriosam, nisi ut aliquid ex ea commodi consequatur? Quis autem vel eum iure reprehenderit qui in ea voluptate velit esse quam nihil molestiae consequatur, vel illum qui dolorem eum fugiat quo</p>
<div class="btn" style="left:112px;top:1149px;width:223px">LEARN MORE
  <svg width="40" height="40" viewBox="0 0 40 40"><circle cx="22" cy="20" r="15" fill="#fff"/><path d="M16 9q8 11 2 22M25 6q7 12 1 27" fill="none" stroke="#e41f26" stroke-width="2"/></svg>
</div>
<div class="abs about-photo" role="img" aria-label="Photo of a young pitcher in a red jersey mid-throw on a grass field"></div>

<!-- stats -->
<section class="abs stats" role="img" aria-label="Dim photo of a pitcher on a field behind the statistics">
  <h2>CHAMPIONSHIPS ARE WON IN PRACTICE</h2>
  <div class="stat" style="left:111px">
    <div class="stat-icon"><svg width="50" height="50" viewBox="0 0 50 50" fill="none" stroke="#fff" stroke-width="2"><circle cx="25" cy="12" r="5"/><circle cx="11" cy="18" r="4"/><circle cx="39" cy="18" r="4"/><circle cx="25" cy="34" r="9"/><path d="M4 34q7-10 14-6M46 34q-7-10-14-6"/></svg></div>
    <div class="stat-num">100+</div>
    <h3>MEMBERSHIP</h3>
    <p>Neque porro quisquam est, qui dolorem ipsum quia dolor sit amet, consectetur, adipisci velit, sed quia</p>
  </div>
  <div class="stat" style="left:452px">
    <div class="stat-icon"><svg width="50" height="50" viewBox="0 0 50 50" fill="none" stroke="#fff" stroke-width="2"><circle cx="25" cy="16" r="11"/><path d="M18 30l-3 8h20l-3-8M12 38h26v6H12z"/></svg></div>
    <div class="stat-num">90+</div>
    <h3>CHAMPION</h3>
    <p>Neque porro quisquam est, qui dolorem ipsum quia dolor sit amet, consectetur, adipisci velit, sed quia</p>
  </div>
  <div class="stat" style="left:798px">
    <div class="stat-icon"><svg width="50" height="50" viewBox="0 0 50 50" fill="none" stroke="#fff" stroke-width="2"><rect x="5" y="8" width="24" height="18"/><circle cx="36" cy="14" r="4"/><path d="M30 44V24h12v20M6 44h38M10 20l8-6 6 4"/></svg></div>
    <div class="stat-num">35+</div>
    <h3>EXPERT COACH</h3>
    <p>Neque porro quisquam est, qui dolorem ipsum quia dolor sit amet, consectetur, adipisci velit, sed quia</p>
  </div>
</section>

<!-- team -->
<div class="abs team-player" role="img" aria-label="Photo of a pitcher in a red jersey holding a glove"></div>
<h2 class="section-title" style="top:1870px;left:122px">OUR TEAM</h2>
<p class="abs team-intro">Neque porro quisquam est, qui dolorem ipsum quia dolor sit amet, consectetur, adipisci velit, sed quia non numquam eius modi tempora</p>
<div class="member one" role="img" aria-label="Portrait photo of a coach in a suit"></div>
<div class="member two" role="img" aria-label="Portrait photo of a team member with name overlay">
  <h4>LOREM LIPSUM</h4>
  <p>General Manager</p>
  <div class="social dark"><span></span><span></span><span></span></div>
</div>
<div class="member three" role="img" aria-label="Portrait photo of a smiling team member with a phone"></div>
<div class="abs dots"><span></span><span class="on"></span><span></span></div>

<!-- portfolio -->
<h2 class="section-title" style="top:2442px">PORTFOLIO</h2>
<div class="tile t1" role="img" aria-label="Photo of a batter swinging at a stadium"></div>
<div class="tile t2" role="img" aria-label="Photo of a pitcher with a dark hover overlay">
  <svg width="30" height="30" viewBox="0 0 30 30" fill="none" stroke="#ddd" stroke-width="2"><path d="M2 10V2h8M2 2l8 8M28 10V2h-8M28 2l-8 8M2 20v8h8M2 28l8-8M28 20v8h-8M28 28l-8-8"/></svg>
</div>
<div class="tile t3" role="img" aria-label="Photo of a hand holding a baseball"></div>
<div class="tile t4" role="img" aria-label="Photo of a pitcher throwing in front of a crowd"></div>
<div class="tile t5" role="img" aria-label="Photo of a pitcher gripping a ball close up"></div>
<div class="tile t6" role="img" aria-label="Photo of a baseball resting on a stadium field"></div>

<!-- contact -->
<h2 class="section-title" style="top:3146px">CONTACT US</h2>
<div class="field" style="left:267px;top:3227px;width:326px">FIRST NAME</div>
<div class="field" style="left:609px;top:3227px;width:325px">LAST NAME</div>
<div class="field" style="left:267px;top:3301px;width:326px">EMAIL ADDRESS</div>
<div class="field" style="left:609px;top:3301px;width:325px">MOBILE NUMBER</div>
<div class="field" style="left:267px;top:3376px;width:667px">TYPE YOUR MESSAGE</div>
<div class="btn" style="left:451px;top:3485px;width:298px">REQUEST SESSIONS
  <svg width="40" height="40" viewBox="0 0 40 40"><circle cx="22" cy="20" r="15" fill="#fff"/><path d="M16 9q8 11 2 22M25 6q7 12 1 27" fill="none" stroke="#e41f26" stroke-width="2"/></svg>
</div>

<!-- footer -->
<svg class="abs footer-bg" width="1200" height="455" viewBox="0 0 1200 455"><path d="M0 92Q600 -90 1200 92V455H0z" fill="#03050a"/></svg>
<div class="abs footer-brand">Delvane Pitching Mechanics</div>
<svg class="abs" style="left:175px;top:3802px" width="24" height="18" viewBox="0 0 26 20"><rect x="1" y="1" width="24" height="18" fill="none" stroke="#fff" stroke-width="2"/><path d="M1 1l12 10 12-10" fill="none" stroke="#fff" stroke-width="2"/></svg>
<div class="f-item" style="left:224px"><b>EMAIL US</b>BOOK@DELVANEPM.COM</div>
<div class="f-div" style="left:413px"></div>
<svg class="abs" style="left:481px;top:3800px" width="22" height="22" viewBox="0 0 24 24"><path d="M5 2l4 5-2 3c1 3 4 6 7 7l3-2 5 4-3 4C10 22 2 14 1 5z" fill="none" stroke="#fff" stroke-width="2"/></svg>
<div class="f-item" style="left:528px"><b>CALL US</b>+1 555 014 2200</div>
<div class="f-div" style="left:716px"></div>
<svg class="abs" style="left:780px;top:3796px" width="20" height="28" viewBox="0 0 20 28"><path d="M10 27S1 15 1 10a9 9 0 0118 0c0 5-9 17-9 17z" fill="#fff"/><circle cx="10" cy="10" r="3.5" fill="#03050a"/></svg>
<div class="f-item" style="left:825px"><b>REACH US</b>24, DELVANE LOREM LIPSUM SIT</div>
<div class="abs f-nav">HOME<i>I</i>ABOUT US<i>I</i>TEAM<i>I</i>PORTFOLIO<i>I</i>CONTACT US</div>
<div class="abs social dark" style="left:531px;top:3937px"><span></span><span></span><span></span></div>
<div class="abs copy">@2023 COPYRIGHTS<i>I</i>DELVANE PITCHING MECHANICS<i>I</i>ALL RIGHTS RESERVED</div>

</body>
</html>
```